Bookkeeping Service Needs Postcard Design for Naturopaths

Looking for a postcard design targeted to naturopaths in the Portland, Oregon metro area.
Below is the text for front and back:
FRONT: You care for your patients. Let me care for your books.
BACK: Hiring an outside bookkeeper saves you time and money.
• No more second-guessing what your CPA and the IRS expect
• No more hours lost to maintaining your books
• No more questions about your financial health
• Accurate, individualized services available
• FREE 1-hour initial consultation
Call: 503-555-0187
Visit: www.larchvaleledgers.example
My business info:
Larchvale Ledgers
P.O. Box 40537
Portland, OR 97291
Logo attached. I have .ai, .psd and .eps files available if needed.
Looking for a design that is warm and eye-catching.
I am looking for a designer I can work with again to design more targeted postcards.
Target Market(s)
Naturopaths
Industry/Entity Type
Alternative Medicine

```html
<!DOCTYPE html>
<html lang="en">
<head>
<meta charset="utf-8">
<title>Larchvale Ledgers Postcard</title>
<link rel="stylesheet" href="https://fonts.googleapis.com/css2?family=Open+Sans:wght@400;600;700;800&display=swap">
<style>
  :root {
    --navy: #1c3f94;
    --blue: #2a63c4;
    --sky: #3c8fd8;
    --teal: #12a7c0;
    --teal-light: #7fd3e0;
    --ink: #1f2a44;
    --paper: #ffffff;
    --backdrop: #e9e6e1;
    --rule: #c9ccd3;
  }
  * { box-sizing: border-box; margin: 0; padding: 0; }
  html, body { width: 839px; height: 1200px; overflow: hidden; }
  body {
    background: var(--backdrop);
    font-family: "Open Sans", Arial, sans-serif;
    color: var(--ink);
    position: relative;
  }
  .postcard {
    position: absolute;
    left: 40px;
    width: 759px;
    height: 516px;
    background: var(--paper);
    overflow: hidden;
    box-shadow: 0 4px 14px rgba(0,0,0,.18);
  }
  .postcard--front { top: 50px; }
  .postcard--back { top: 634px; }

  /* Front */
  .front-photo {
    position: absolute; inset: 0 0 120px 0;
    background: linear-gradient(180deg, #eaf4fb 0%, #cfe6f5 45%, #7cbfe3 70%, #2f86c6 100%);
  }
  .front-photo::after {
    content: ""; position: absolute; left: 250px; top: 110px; width: 240px; height: 230px;
    border-radius: 50%;
    background: radial-gradient(circle, rgba(122,190,60,.85) 0%, rgba(122,190,60,.45) 45%, rgba(122,190,60,0) 72%);
  }
  .front-headline {
    position: absolute; top: 34px; left: 0; right: 0;
    text-align: center; font-size: 36px; line-height: 1.2; font-weight: 600;
    color: var(--sky); letter-spacing: .3px;
  }
  .front-headline strong { color: var(--navy); font-weight: 800; }
  .front-swoosh { position: absolute; left: 0; bottom: 0; width: 759px; height: 200px; }
  .brand {
    position: absolute; left: 30px; bottom: 26px;
    display: flex; align-items: center; gap: 12px;
  }
  .brand-dot {
    width: 40px; height: 40px; border-radius: 50%;
    border: 3px solid var(--blue); flex: none;
  }
  .brand-name { font-size: 28px; font-weight: 700; color: var(--navy); line-height: 1; }
  .front-url {
    position: absolute; right: 34px; bottom: 30px;
    font-size: 16px; color: var(--navy); font-weight: 600;
  }

  /* Back */
  .back-divider { position: absolute; left: 0; top: 0; width: 759px; height: 516px; }
  .back-headline {
    position: absolute; left: 40px; top: 32px; width: 390px;
    font-size: 24px; font-weight: 800; color: var(--navy); line-height: 1.25;
  }
  .benefits {
    position: absolute; left: 40px; top: 128px; width: 400px;
    list-style: none; font-size: 14.5px; line-height: 1.3; color: var(--ink);
  }
  .benefits li { position: relative; padding-left: 22px; margin-bottom: 7px; }
  .benefits li::before {
    content: ""; position: absolute; left: 0; top: 4px;
    width: 11px; height: 11px; border-radius: 50%; background: var(--blue);
  }
  .back-photo {
    position: absolute; left: 0; top: 300px; width: 440px; height: 110px;
    background: linear-gradient(90deg, #c9d3dc 0%, #eef1f3 45%, #dfe4e8 75%, #b7c0c8 100%);
  }
  .call {
    position: absolute; left: 0; top: 420px; width: 440px; text-align: center;
  }
  .call-lead { font-size: 20px; color: var(--sky); font-weight: 600; }
  .call-phone {
    display: inline-flex; align-items: center; gap: 8px;
    font-size: 24px; font-weight: 800; color: var(--navy); margin-top: 2px;
  }
  .call-phone svg { width: 22px; height: 22px; }
  .call-url { font-size: 14px; color: var(--navy); margin-top: 4px; font-weight: 600; }
  .stamp-box {
    position: absolute; right: 32px; top: 30px; width: 70px; height: 80px;
    border: 1.5px solid var(--rule);
  }
  .address-lines { position: absolute; right: 32px; top: 250px; width: 230px; }
  .address-lines span { display: block; border-bottom: 1.5px solid var(--rule); height: 32px; }
</style>
</head>
<body>

<section class="postcard postcard--front">
  <div class="front-photo" role="img" aria-label="Photo of a green leaf floating like a boat on calm blue water"></div>
  <h1 class="front-headline">
    <strong>YOU CARE</strong> FOR YOUR PATIENTS.<br>
    <strong>LET ME CARE</strong> FOR YOUR BOOKS.
  </h1>
  <svg class="front-swoosh" viewBox="0 0 759 200" preserveAspectRatio="none" aria-hidden="true">
    <path d="M0 80 C200 30 420 140 759 50 L759 200 L0 200 Z" fill="var(--teal-light)" opacity=".7"/>
    <path d="M0 95 C220 50 430 150 759 72 L759 200 L0 200 Z" fill="var(--teal)"/>
    <path d="M0 110 C230 70 440 160 759 92 L759 200 L0 200 Z" fill="var(--paper)"/>
  </svg>
  <div class="brand">
    <span class="brand-dot"></span>
    <span class="brand-name">Larchvale Ledgers</span>
  </div>
  <div class="front-url">www.larchvaleledgers.example</div>
</section>

<section class="postcard postcard--back">
  <svg class="back-divider" viewBox="0 0 759 516" preserveAspectRatio="none" aria-hidden="true">
    <path d="M440 0 L468 0 C520 120 520 380 452 516 L440 516 Z" fill="var(--teal)"/>
    <path d="M470 0 L480 0 C535 130 530 380 462 516 L454 516 C520 380 522 130 470 0 Z" fill="var(--teal-light)"/>
  </svg>
  <h2 class="back-headline">HIRING AN OUTSIDE BOOKKEEPER SAVES YOU TIME AND MONEY.</h2>
  <ul class="benefits">
    <li>No more second-guessing what your CPA and the IRS expect</li>
    <li>No more hours lost to maintaining your books</li>
    <li>No more questions about your financial health</li>
    <li>Accurate, individualized services available</li>
    <li>FREE 1-hour initial consultation</li>
  </ul>
  <div class="back-photo" role="img" aria-label="Photo of a hand writing in a ledger beside a calculator"></div>
  <div class="call">
    <div class="call-lead">Call us now!</div>
    <div class="call-phone">
      <svg viewBox="0 0 24 24" aria-hidden="true">
        <circle cx="12" cy="12" r="12" fill="var(--navy)"/>
        <path d="M8.2 6.5c.4-.3 1-.2 1.3.2l1.2 1.8c.3.4.2 1-.2 1.3l-.8.6c.6 1.3 1.6 2.4 2.9 3l.6-.8c.3-.4.9-.5 1.3-.2l1.8 1.2c.4.3.5.9.2 1.3l-.7 1c-.5.6-1.3.8-2 .5-3-1.2-5.4-3.6-6.6-6.6-.3-.7-.1-1.5.5-2z" fill="#fff"/>
      </svg>
      503-555-0187
    </div>
    <div class="call-url">www.larchvaleledgers.example</div>
  </div>
  <div class="stamp-box"></div>
  <div class="address-lines"><span></span><span></span><span></span><span></span></div>
</section>

</body>
</html>
```